Business Intelligence Application - Reporting Menu and Report Criteria Design

Looking for a fresh, effective and user friendly view for the menu structure and reporting criteria screen format for a business reporting application. Initial format completed, content structure is in place, but we need the 'wow' design.. as its a serious professional report/BI tool it has to fall within certain guidelines for clarity and graphics..but we want it to be slick, friendly, great user experience. There is a large amount of complex content to fit into a small space and we need it to be very inviting, modern and intuitive.. If interested, please review the attachment. We have live screens in operation, but feel these could be improved and looking forward to seeing what great creative suggestions could be made. Please review work done to date in the attached.. We are not looking for a total re-design of everything, all the basic business content/structure is there.. but tell us what we could do to improve this in terms of graphic design... particularly the criteria screens.. thanks!
Updates

Reason: Need a few more days to review designs - thanks for all submissions so far, we will make a selection shortly.

Target Market(s)

Business analysts, hotel operations teams, finance analysts hospitality industry

Industry/Entity Type

Hospitality

Coding

Coded - Design and coding required

Number of Pages Required

4 page

Font styles to use
Sans Serif
Other font styles liked:
• Candara, please see example in deck

Colors
3276b5
3176b5
0255a3
85acd3
33a6d7
cee9f5
85cae6

Requirements
Must have
• sharp clear, logical menu structure, (currently it has 'clicks to sub-menus, we need hover over, slide to sub-menus..) colour, styling.. and most focus on revision of criteria.. right now is somewhat heavy, cumbersome.. keep colour and friendly intuitive process steps.. its heavy analytical stuff.. best of luck!
Should not have
• No grey fonts on white or grey screens! many business apps are not readable or sharp.. or fonts are too small.. colourless, so please avoid that.. see our deck - sharp dark (navy) or black fonts on white, or light shading..

```html
<!DOCTYPE html>
<html lang="en">
<head>
<meta charset="utf-8">
<title>Silver Bay Hotel &amp; Suites – Reporting Menu</title>
<link rel="stylesheet" href="https://fonts.googleapis.com/css2?family=Mukta:wght@400;500;600&display=swap">
<style>
  :root {
    --sky: #33a6d7;
    --sky-pale: #d0e8f5;
    --navy-ink: #111a24;
    --white: #ffffff;
    --divider: rgba(255,255,255,0.35);
    --search-border: #b9c3cb;
  }
  * { box-sizing: border-box; margin: 0; padding: 0; }
  html, body { width: 1200px; height: 422px; overflow: hidden; background: var(--white); }
  body { position: relative; font-family: "Mukta", "Candara", sans-serif; color: var(--navy-ink); }

  .topbar { position: absolute; left: 0; top: 0; width: 1200px; height: 60px; background: var(--sky-pale); }
  .brand { position: absolute; left: 48px; top: 15px; display: flex; align-items: center; gap: 10px; }
  .brand-mark { width: 26px; height: 26px; border-radius: 50%; background: var(--sky); }
  .brand-name { font-size: 19px; font-weight: 500; color: var(--sky); letter-spacing: -0.2px; line-height: 1; }
  .welcome, .today { position: absolute; top: 21px; font-size: 13px; font-weight: 500; line-height: 18px; }
  .welcome { left: 555px; }
  .today { left: 668px; }
  .top-btn { position: absolute; top: 11px; height: 37px; width: 108px; background: var(--sky); color: var(--white);
    font-size: 12.5px; font-weight: 500; letter-spacing: 0.4px; display: flex; align-items: center; justify-content: center; }
  .btn-intel { left: 834px; }
  .btn-planning { left: 956px; }
  .top-icon { position: absolute; top: 18px; }
  .icon-bell { left: 1083px; }
  .icon-share { left: 1124px; }

  .main-nav { position: absolute; left: 47px; top: 88px; display: flex; align-items: center; font-size: 13px; font-weight: 500; line-height: 20px; white-space: nowrap; }
  .main-nav .sep { color: var(--sky); margin: 0 7px; font-size: 10px; }
  .main-nav .active { color: var(--sky); }

  .search { position: absolute; left: 775px; top: 81px; width: 373px; height: 37px; border: 1px solid var(--search-border);
    display: flex; align-items: center; padding: 0 12px 0 17px; font-size: 11.5px; letter-spacing: 0.3px; }
  .search span { flex: 1; }

  .sub-nav { position: absolute; left: 332px; top: 130px; width: 430px; height: 37px; background: var(--sky); color: var(--white);
    display: flex; align-items: center; padding-left: 14px; font-size: 12.5px; font-weight: 500; white-space: nowrap; }
  .sub-nav .sep { margin: 0 8px; font-size: 9px; }
  .pointer { position: absolute; width: 0; height: 0; border-left: 9px solid transparent; border-right: 9px solid transparent; border-bottom: 9px solid var(--sky); }
  .sub-nav .pointer { left: 15px; top: -9px; }

  .flyout { position: absolute; top: 190px; width: 163px; background: var(--sky); color: var(--white); box-shadow: 0 4px 10px rgba(0,0,0,0.12); list-style: none; }
  .flyout .pointer { left: 12px; top: -9px; }
  .flyout-primary { left: 48px; }
  .flyout-secondary { left: 224px; }
  .flyout li { height: 33.6px; display: flex; align-items: center; justify-content: space-between; padding: 0 11px; font-size: 11px; border-top: 1px solid var(--divider); }
  .flyout li:first-of-type { border-top: none; }
  .caret { width: 0; height: 0; border-top: 4px solid transparent; border-bottom: 4px solid transparent; border-left: 5px solid var(--white); }
</style>
</head>
<body>
  <header class="topbar">
    <div class="brand"><span class="brand-mark"></span><span class="brand-name">Silver Bay Hotel &amp; Suites</span></div>
    <div class="welcome">Welcome Admin</div>
    <div class="today">Tuesday October 04.2017</div>
    <div class="top-btn btn-intel">INTEL</div>
    <div class="top-btn btn-planning">PLANNING</div>
    <svg class="top-icon icon-bell" width="26" height="24" viewBox="0 0 26 24" fill="none" stroke="#111a24" stroke-width="1.3" stroke-linejoin="round">
      <path d="M8 17 V11 a5 5 0 0 1 10 0 V17 l2 2 H6 z"/>
      <path d="M11 20.5 a2 2 0 0 0 4 0"/>
      <circle cx="13" cy="4.5" r="1"/>
      <path d="M3.5 9 q-1.5 3 0 6 M22.5 9 q1.5 3 0 6"/>
    </svg>
    <svg class="top-icon icon-share" width="28" height="22" viewBox="0 0 28 22" fill="none" stroke="#111a24" stroke-width="1.3" stroke-linejoin="round">
      <path d="M19 8 H6 q-4 0 -4 4 V20 H20 V14"/>
      <path d="M8 15 q2 -7 11 -7 V4 l7 6 l-7 6 V12 q-7 -1 -11 3 z"/>
    </svg>
  </header>

  <nav class="main-nav">
    <span>Admin</span><span class="sep">•</span>
    <span class="active">Management</span><span class="sep">•</span>
    <span class="active">Rooms Performance</span><span class="sep">•</span>
    <span class="active">Revenue Summary</span><span class="sep">•</span>
    <span>Demand &amp; Risk</span><span class="sep">•</span>
    <span>Inventory Analysis</span><span class="sep">•</span>
    <span>Placeholder</span>
  </nav>

  <div class="search">
    <span>PROPERTY SEARCH</span>
    <svg width="14" height="14" viewBox="0 0 14 14" fill="none" stroke="#111a24" stroke-width="1.3"><circle cx="6" cy="6" r="4.8"/><path d="M9.5 9.5 L13 13"/></svg>
  </div>

  <nav class="sub-nav">
    <span class="pointer"></span>
    <span>Rollup Criteria</span><span class="sep">•</span>
    <span>Report Criteria</span><span class="sep">•</span>
    <span>Edit View</span><span class="sep">•</span>
    <span>Saved View</span><span class="sep">•</span>
    <span>Export</span>
  </nav>

  <ul class="flyout flyout-primary">
    <span class="pointer"></span>
    <li>Summaries<span class="caret"></span></li>
    <li>Consolidations<span class="caret"></span></li>
    <li>Communication<span class="caret"></span></li>
    <li>Cheat Sheets<span class="caret"></span></li>
    <li>Programs<span class="caret"></span></li>
  </ul>

  <ul class="flyout flyout-secondary">
    <span class="pointer"></span>
    <li>Commpany Review</li>
    <li>Rooms Performance</li>
    <li>F&amp;B Performance</li>
    <li>Competitive Review</li>
    <li>Operations</li>
  </ul>
</body>
</html>
```